Business Card Design

We need a new business card design for our company, Lumen Forge.

Our website: www.brightrow7.ca

We are open to all ideas, from professional to very creative.
Updates

Design update requests:

1. We would like to see some examples with "BrightRow7" instead of "Lumen Forge" as the company name.
2. Would like to see "Software | Web | Branding" included on the card somewhere as well.

Thanks.

We are really trying to express the nature of our business through our business card.  "Lumen" can be misconstrued for the health industry, so use of "BrightRow7" and the "Software | Web | Branding" slogan are key to understanding our business.

We have uploaded a new PSD which includes a monitor, tablet, and phone screen.  This represents the flexibility of web applications and is another tool we would like to see used on business cards.

We will be eliminating designs today and will await updated designs with these new specs.

Thank-you.

Industry/Entity Type

Business

Requirements
Must have
• Content:
First M. Last
Managing Partner
e. email@brightrow7.ca
p. 555.555.5555

```html
<!DOCTYPE html>
<html lang="en">
<head>
<meta charset="utf-8">
<title>Lumen Forge – Business Card</title>
<link rel="stylesheet" href="https://fonts.googleapis.com/css2?family=Michroma&display=swap">
<style>
  :root {
    --backdrop: #e4e6e8;
    --card-dark: #3b3b3c;
    --card-light: #fdfdfd;
    --ink-dark: #3a3a3a;
    --ink-light: #f4f4f4;
    --ink-muted: #c9c9c9;
    --accent: #27a9e1;
    --accent-deep: #1f5d78;
    --accent-pale: #a8dcf3;
    --tile-dark: #4a5961;
  }
  * { box-sizing: border-box; margin: 0; padding: 0; }
  html, body { width: 1200px; height: 800px; overflow: hidden; }
  body { background: var(--backdrop); font-family: "Michroma", sans-serif; }

  .canvas { position: relative; width: 1200px; height: 800px; overflow: hidden; }

  .card {
    position: absolute;
    left: 290px;
    width: 620px;
    height: 354px;
    overflow: hidden;
    box-shadow: 0 6px 18px rgba(0,0,0,0.18);
  }
  .card--back  { top: 30px;  background: var(--card-dark); }
  .card--front { top: 416px; background: var(--card-light); }

  .tile-field { position: absolute; top: 0; left: 0; }

  /* back side */
  .back-brand {
    position: absolute;
    left: 0; width: 450px; top: 118px;
    text-align: center;
    color: var(--ink-light);
    font-size: 34px;
    letter-spacing: 2px;
    text-transform: uppercase;
  }
  .back-tagline {
    position: absolute;
    left: 0; width: 450px; top: 200px;
    text-align: center;
    color: var(--ink-muted);
    font-size: 13px;
    letter-spacing: 5px;
  }
  .back-tagline .sep { margin: 0 10px; color: #8a8a8a; }
  .back-url {
    position: absolute;
    left: 0; width: 450px; top: 236px;
    text-align: center;
    color: var(--ink-muted);
    font-size: 9px;
    letter-spacing: 3px;
    text-transform: uppercase;
  }

  /* front side */
  .front-brand {
    position: absolute;
    left: 360px; top: 110px;
    display: flex; align-items: center; gap: 12px;
  }
  .front-brand__mark { width: 26px; height: 26px; background: var(--accent); }
  .front-brand__name {
    color: var(--ink-dark);
    font-size: 20px;
    letter-spacing: 1px;
    text-transform: uppercase;
    line-height: 1.15;
  }

  .person { position: absolute; left: 70px; top: 258px; }
  .person__name { color: var(--accent); font-size: 17px; letter-spacing: 1px; font-variant: small-caps; }
  .person__role { margin-top: 2px; padding-left: 8px; color: #5a5a5a; font-size: 7.5px; letter-spacing: 1.5px; text-transform: uppercase; }

  .divider { position: absolute; left: 300px; top: 250px; width: 2px; height: 56px; background: var(--accent); }

  .contact { position: absolute; left: 330px; top: 254px; list-style: none; }
  .contact__item {
    display: flex; align-items: center; gap: 10px;
    color: var(--accent-deep);
    font-size: 12px; letter-spacing: 1.5px;
    height: 24px;
  }
  .contact__item--email { font-size: 10px; text-transform: uppercase; }
  .contact__icon { width: 16px; height: 16px; flex: none; }
</style>
</head>
<body>
<main class="canvas">

  <section class="card card--back" aria-label="Business card, back">
    <svg class="tile-field" width="620" height="354" viewBox="0 0 620 354" role="img" aria-label="Faint tile mosaic area">
      <defs>
        <linearGradient id="backTiles" x1="0" y1="0" x2="1" y2="1">
          <stop offset="0" stop-color="var(--tile-dark)" stop-opacity="0.55"/>
          <stop offset="1" stop-color="var(--tile-dark)" stop-opacity="0.9"/>
        </linearGradient>
      </defs>
      <polygon points="470,70 620,20 620,354 560,354 520,300 500,200 470,150" fill="url(#backTiles)"/>
    </svg>
    <div class="back-brand">Lumen Forge</div>
    <div class="back-tagline">SOFTWARE<span class="sep">|</span>WEB<span class="sep">|</span>BRANDING</div>
    <div class="back-url">www.brightrow7.ca</div>
  </section>

  <section class="card card--front" aria-label="Business card, front">
    <svg class="tile-field" width="620" height="354" viewBox="0 0 620 354" role="img" aria-label="Blue tile mosaic area">
      <defs>
        <linearGradient id="frontTiles" x1="0" y1="0" x2="1" y2="1">
          <stop offset="0" stop-color="var(--accent-deep)"/>
          <stop offset="0.5" stop-color="var(--accent)"/>
          <stop offset="1" stop-color="var(--accent-pale)"/>
        </linearGradient>
      </defs>
      <polygon points="0,0 300,0 300,110 240,170 170,215 90,250 0,280" fill="url(#frontTiles)"/>
    </svg>

    <div class="front-brand">
      <span class="front-brand__mark"></span>
      <span class="front-brand__name">Lumen Forge</span>
    </div>

    <div class="person">
      <p class="person__name">First M. Last</p>
      <p class="person__role">Managing Partner</p>
    </div>

    <div class="divider"></div>

    <ul class="contact">
      <li class="contact__item">
        <svg class="contact__icon" viewBox="0 0 16 16" aria-hidden="true">
          <rect x="4" y="1" width="8" height="14" rx="1.5" fill="none" stroke="var(--accent)" stroke-width="1.6"/>
          <rect x="6" y="3.5" width="4" height="5" fill="var(--accent)"/>
        </svg>
        555.555.5555
      </li>
      <li class="contact__item contact__item--email">
        <svg class="contact__icon" viewBox="0 0 16 16" aria-hidden="true">
          <rect x="1" y="3" width="14" height="10" fill="none" stroke="var(--accent)" stroke-width="1.6"/>
          <path d="M1 3 L8 9 L15 3" fill="none" stroke="var(--accent)" stroke-width="1.6"/>
        </svg>
        email@brightrow7.ca
      </li>
    </ul>
  </section>

</main>
</body>
</html>
```